Not Your Average Diet Book Cover Design

I need a book cover designed for a project titled:
Title: Table Route Junction
Sub-title: The Hidden Key To Gently Mastering Your Meals
Author: Carla Brightwood
Designation: Not a Doctor
The book is a look at 8 trendy diets (Atkins, Whole Foods, Paleo, Keto, Mediterranean, Sugar Free, Alkaline and Intermittent Fasting), with each chapter covering the pros and cons of one.
The theme throughout the book is that, when approached as a diet, they are each doomed to failure. When sustainability and lifestyle are taken into consideration, however, any one of them (or a combination of two or more) can lead to overall health and weight management.
Vegetables, mindset and habit creation are 3 of the "overlap" factors implied in the title.
I have uploaded a temporary cover that I am using as a placeholder at the moment. I do NOT want anything like it. (Use the tagline above, not the one in the sample cover).
Please, NO images of scales, stomachs, or anything else that is super cliche for the weight loss industry.
This is a full length book, written in a conversation tone, that I want to stand out from the a) copy and pasted online "experts" and b) doctors and fitpros who think it's their way or the highway. I want it to be welcoming and accessible.
I want the book to appeal to an audience who is currently struggling with their health and most likely failed at many diets in the past.
I will need a print cover for a 6"x 9" Pressbloom book, as well as a Lumora cover and an Sonvera cover.
I would like all source files, including any fonts used. For delivery, placeholder text can be used for the back cover.
Target Market(s)
Male & Female
Overweight
Unhealthy, but not severely so
Have tried diets before and failed
Age: 25-55 (average)
Income: $30-50k USD
Marital status: Single OR not entirely satisfied with the relationship
Location: Canada, USA, Australia, UK
Industry/Entity Type
Health And Wellness
Colors
Designer to choose colors to be used in the design.
Requirements
Must have
- Title: Table Route Junction
- Sub-title: The Hidden Key To Gently Mastering Your Meals
- Author: Carla Brightwood
- Designation: Not a Doctor
Nice to have
- A welcoming, understanding feeling
- Implications of holistic health
Should not have
- Images:
- - Scale or measuring tapes, etc
- - stomachs/abs
- - yoga or any silhouettes
- A look similar to the sample.

```html
<!DOCTYPE html>
<html lang="en">
<head>
<meta charset="utf-8">
<title>Table Route Junction – Full Cover Wrap</title>
<link rel="stylesheet" href="https://fonts.googleapis.com/css2?family=Playfair+Display:wght@400;500&family=Dosis:wght@500&family=Nunito+Sans:wght@600&display=swap">
<style>
  :root {
    --page: #ffffff;
    --peach: #f5b48f;
    --mist: #f4f3ef;
    --lemon: #f0e664;
    --aqua: #b3dcd6;
    --kiwi: #a6c94a;
    --kiwi-deep: #6ea12a;
    --pepper: #e65a4c;
    --ink: #1b2131;
    --leaf: #1c7a2c;
    --shrimp: #f08a5c;
    --fish: #3c7f96;
    --corn: #f4de7a;
    --skin: #e7c0a0;
  }
  * { margin: 0; padding: 0; box-sizing: border-box; }
  html, body { width: 1200px; height: 1200px; overflow: hidden; background: var(--page); }

  .cover-wrap {
    position: absolute; left: 40px; top: 195px;
    width: 1120px; height: 810px; overflow: hidden;
    box-shadow: 0 6px 18px rgba(0,0,0,0.18);
    background: var(--mist);
  }
  .band, .photo { position: absolute; }
  .band--peach { left: 0; top: 0; width: 816px; height: 138px; background: var(--peach); }
  .band--mist { left: 0; top: 138px; width: 830px; height: 137px; background: var(--mist); }
  .band--lemon { left: 0; top: 275px; width: 1000px; height: 266px; background: var(--lemon); }
  .band--aqua { left: 0; top: 541px; width: 830px; height: 269px; background: var(--aqua); }

  .photo--shrimp { left: 480px; top: 0; width: 300px; height: 138px;
    background: radial-gradient(ellipse at 50% 50%, var(--shrimp) 0 35%, var(--peach) 70%); }
  .photo--stride { left: 663px; top: 138px; width: 167px; height: 137px;
    background: linear-gradient(180deg, #e9ddd2, #f3ead0); }
  .photo--kiwi { left: 816px; top: 0; width: 304px; height: 254px;
    background: radial-gradient(circle at 30% 30%, var(--kiwi) 0 25%, var(--kiwi-deep) 40%, var(--kiwi) 60%); }
  .photo--pepper { left: 1000px; top: 254px; width: 120px; height: 283px;
    background: linear-gradient(90deg, var(--pepper), #c9362d); }
  .photo--corn { left: 555px; top: 275px; width: 148px; height: 268px;
    background: linear-gradient(90deg, #f6e9a8, var(--corn), #f6e9a8); }
  .photo--fish { left: 393px; top: 628px; width: 437px; height: 120px;
    background: radial-gradient(ellipse at 55% 50%, var(--fish) 0 30%, var(--aqua) 72%); }
  .photo--hand { left: 830px; top: 537px; width: 290px; height: 273px;
    background: linear-gradient(160deg, #f2dd8a 0%, var(--skin) 45%, #d9e4e8 75%, #2f3a52 100%); }

  .back-blurb {
    position: absolute; left: 130px; top: 343px; width: 300px;
    font-family: "Nunito Sans", sans-serif; font-weight: 600;
    font-size: 14.5px; line-height: 20.5px; color: #161616; text-align: center;
  }
  .barcode-space { position: absolute; left: 174px; top: 664px; width: 207px; height: 101px; background: #ffffff; }

  .spine-text {
    position: absolute; writing-mode: vertical-rl;
    font-family: "Playfair Display", serif; color: var(--ink); font-size: 21px;
  }
  .spine-text--author { left: 542px; top: 42px; }
  .spine-text--title { left: 542px; top: 296px; }

  .title-badge {
    position: absolute; left: 640px; top: 176px; width: 452px; height: 452px;
    border-radius: 50%; background: #f7f7f5;
    box-shadow: 0 2px 10px rgba(0,0,0,0.12);
  }
  .book-title {
    position: absolute; left: 0; top: 0;
    font-family: "Playfair Display", serif; font-weight: 400;
    color: var(--ink); font-size: 84px; line-height: 1;
  }
  .book-title span { position: absolute; white-space: nowrap; }
  .book-title .line-1 { left: 706px; top: 243px; }
  .book-title .line-2 { left: 800px; top: 306px; }
  .book-title .line-3 { left: 684px; top: 381px; }
  .subtitle {
    position: absolute; left: 700px; top: 470px; width: 332px;
    font-family: "Dosis", sans-serif; font-weight: 500;
    font-size: 25px; line-height: 28.5px; color: var(--leaf); text-align: center;
  }
  .author-block {
    position: absolute; left: 730px; top: 738px; width: 220px; text-align: center;
  }
  .author-name { font-family: "Playfair Display", serif; font-size: 19px; color: var(--ink); display: block; }
  .author-role { font-family: "Nunito Sans", sans-serif; font-size: 10px; color: var(--leaf); display: block; margin-top: -2px; }
</style>
</head>
<body>
  <main class="cover-wrap">
    <div class="band band--peach"></div>
    <div class="band band--mist"></div>
    <div class="band band--lemon"></div>
    <div class="band band--aqua"></div>

    <div class="photo photo--shrimp" role="img" aria-label="Photo of a cooked shrimp"></div>
    <div class="photo photo--stride" role="img" aria-label="Photo of a person's legs walking"></div>
    <div class="photo photo--kiwi" role="img" aria-label="Photo of sliced kiwi fruit"></div>
    <div class="photo photo--pepper" role="img" aria-label="Photo of a red chili pepper"></div>
    <div class="photo photo--corn" role="img" aria-label="Photo of a corn cob"></div>
    <div class="photo photo--fish" role="img" aria-label="Photo of two fresh sardines"></div>
    <div class="photo photo--hand" role="img" aria-label="Photo of a hand holding a water bottle"></div>

    <p class="back-blurb">Lorem ipsum dolor sit amet, consectetuer adipiscing elit, sed diam nonummy nibh euismod tincidunt ut laoreet dolore magna aliquam erat volutpat. Ut wisi enim ad minim veniam, quis nostrud exerci tation ullamcorper suscipit lobortis nisl ut aliquip ex ea commodo consequat.</p>
    <div class="barcode-space"></div>

    <span class="spine-text spine-text--author">C. Brightwood</span>
    <span class="spine-text spine-text--title">Table Route Junction</span>

    <div class="title-badge"></div>
    <h1 class="book-title">
      <span class="line-1">Table</span>
      <span class="line-2">Route</span>
      <span class="line-3">Junction</span>
    </h1>
    <p class="subtitle">The Hidden Key<br>To Gently Mastering<br>Your Meals</p>
    <p class="author-block">
      <span class="author-name">Carla Brightwood</span>
      <span class="author-role">Not a Doctor</span>
    </p>
  </main>
</body>
</html>
```